依頼詳細
ラベルのデザインを募集します。

基本的には、幅91.5mm 縦131mmの縦長で角が少し丸いシールにいれるデザインです
・データは様々な形で使用させて頂きます。
(ホームページに載せたり、サンプル品に使用するなど)

クラフトのチャック袋(スタンドパック)にラベルを貼る予定です。
■キャッチフレーズなど
・魔法のスーパーフード タイガーナッツ!パウダータイプ

記載項目
商品名:星屑のコモレビパウダー
その他キャッチフレーズ、キーワードなど:スーパーフード
希望イメージ
シンプル 複雑
単色 カラフル
暗い 明るい
日常 高級
遊び心 厳粛
未来的 伝統的
女性的 男性的
希望する色
赤系、黄・オレンジ系
納品ファイル
• イラストレーター形式 (.ai)
• フォトショップ形式 (.psd)
補足説明
送付ファイルはパウダーの写真です。特に使わなくても大丈夫ですが、色合いなど確認するのにお使いください。
粒状態の画像を追加します。
製品自体は粉なので参考にしてください。
使わなくても大丈夫です。
■ 選んだ理由

自分の考えていたイメージに近く、魔法感がよく出ていて
まとまっていたのでこちらを選ばせて頂きました。

■ 提案者全員のお礼・コメント

多数のご応募ありがとうございました。
またの機会がありましたら、よろしくお願い足します。

```html
<!DOCTYPE html>
<html lang="ja">
<head>
<meta charset="utf-8">
<title>星屑のコモレビパウダー ラベル</title>
<link rel="stylesheet" href="https://fonts.googleapis.com/css2?family=Dela+Gothic+One&family=M+PLUS+Rounded+1c:wght@900&family=Oswald:wght@500&display=swap">
<style>
  :root {
    --page: #f3efe8;
    --frame: #3a2417;
    --red: #d81f1c;
    --red-deep: #a3120f;
    --yellow: #f7d21e;
    --orange: #ef8a15;
    --beige: #eadcb3;
    --brown: #6b4522;
    --white: #ffffff;
    --powder-light: #e2d3b8;
    --powder-dark: #a88e6a;
  }
  html, body {
    margin: 0;
    width: 818px;
    height: 1200px;
    overflow: hidden;
    background: var(--page);
  }
  .label {
    position: absolute;
    left: 29px;
    top: 40px;
    width: 760px;
    height: 1120px;
    border: 12px solid var(--frame);
    border-radius: 34px;
    box-sizing: border-box;
    overflow: hidden;
    background: var(--red);
  }
  .powder-photo {
    position: absolute;
    left: 0; top: 0;
    width: 100%;
    height: 420px;
    background: radial-gradient(ellipse at 40% 45%, var(--powder-light) 0%, #cdb894 55%, var(--powder-dark) 100%);
  }
  .bands {
    position: absolute;
    left: 0; top: 0;
    width: 100%;
    height: 100%;
  }
  .catch {
    position: absolute;
    left: 34px;
    top: 330px;
    margin: 0;
    font-family: "M PLUS Rounded 1c", sans-serif;
    font-weight: 900;
    font-size: 50px;
    line-height: 1.18;
    color: var(--red);
    -webkit-text-stroke: 12px var(--white);
    paint-order: stroke fill;
    transform: rotate(-9deg);
    transform-origin: left top;
  }
  .product-name {
    position: absolute;
    left: 0;
    right: 0;
    top: 500px;
    margin: 0;
    text-align: center;
    font-family: "Dela Gothic One", sans-serif;
    font-weight: 400;
    font-size: 112px;
    line-height: 1.12;
    color: var(--white);
    -webkit-text-stroke: 16px var(--red-deep);
    paint-order: stroke fill;
    letter-spacing: 2px;
  }
  .product-name span { display: block; }
  .product-name .small { font-size: 96px; }
  .ingredient-band {
    position: absolute;
    left: 0; bottom: 0;
    width: 100%;
    height: 236px;
    background: var(--beige);
    border-top: 14px solid var(--yellow);
    box-sizing: border-box;
    display: flex;
    align-items: center;
    justify-content: center;
  }
  .ingredient-name {
    margin: 0;
    font-family: "Oswald", sans-serif;
    font-weight: 500;
    font-size: 118px;
    letter-spacing: 4px;
    color: var(--brown);
  }
</style>
</head>
<body>
  <div class="label">
    <div class="powder-photo" role="img" aria-label="器に盛られたベージュ色のパウダーの写真"></div>
    <svg class="bands" viewBox="0 0 736 1096" preserveAspectRatio="none" aria-hidden="true">
      <polygon points="0,330 736,190 736,1096 0,1096" fill="var(--red)"/>
      <polygon points="0,330 736,190 736,230 0,372" fill="var(--red-deep)"/>
      <polygon points="0,470 736,330 736,372 0,512" fill="var(--yellow)"/>
      <polygon points="0,512 736,372 736,400 0,540" fill="var(--orange)"/>
      <polygon points="0,812 736,760 736,792 0,844" fill="var(--yellow)"/>
      <polygon points="0,844 736,792 736,860 0,860" fill="var(--red-deep)"/>
    </svg>
    <p class="catch">栄養価満点！<br>話題のスーパーフード</p>
    <h1 class="product-name">
      <span>星屑の</span>
      <span>コモレビ</span>
      <span class="small">パウダー</span>
    </h1>
    <div class="ingredient-band">
      <p class="ingredient-name">TIGER NUTS</p>
    </div>
  </div>
</body>
</html>
```